Pelora Vantu Child Care Website

Website designs are required for a new, modern and state of the art Child Care Centre.

Pelora Vantu Child Care is a new Child Care and Long Day Care provider. It provides care, learning and education services for children under 24 months, toddlers and also preschool children.

The website design needs to incorporate elements of care, fun and learning, while displaying the Brand name clearly - i.e easy to read and understand - considering the unusual name...

We would like to see proposals that focus on portraying a professional overall brand identity. It needs to be modern and use fresh colors.

Please see attached logo concept selected.

***NOTE*** Feel free to adjust colors of this logo based on the site theme.

If you require any clarification please feel free to contact us.

Target Market(s)

School teachers
Parents
Parents with young children

Industry/Entity Type

Education

Requirements
Must have
• Responsive design - must support all browsers
Modern and creative - must make use of modern design techniques. See http://dravenmixo.example/ for inspiration!
Should not have
• copied ideas. keep it original

```html
<!DOCTYPE html>
<html lang="en">
<head>
<meta charset="utf-8">
<title>Pelora Vantu Child Care</title>
<link href="https://fonts.googleapis.com/css2?family=Arvo&family=Schoolbell&family=Short+Stack&display=swap" rel="stylesheet">
<style>
  :root {
    --sand: #eee5d5;
    --sand-line: #ddd1bd;
    --mint: #b3e6cb;
    --forest: #1f8a3c;
    --forest-dark: #15702e;
    --leaf: #3f9e4f;
    --orange: #e8711a;
    --pink: #e8388a;
    --sky-blue: #2a9ad6;
    --rose: #d9679a;
    --sea: #4fbf8c;
    --ink: #3d3a33;
    --muted: #6b6458;
    --white: #ffffff;
    --sky-top: #86d3f2;
    --sky-bottom: #c9ecf8;
    --field: #124d1f;
  }
  * { box-sizing: border-box; margin: 0; padding: 0; }
  html, body { width: 736px; height: 1200px; overflow: hidden; background: var(--sand); }
  body { font-family: "Short Stack", cursive; color: var(--ink); }
  .page { position: relative; width: 736px; height: 1200px; overflow: hidden; }
  .abs { position: absolute; }
  .heading { font-family: "Schoolbell", cursive; font-weight: 400; text-transform: uppercase; letter-spacing: .3px; }

  /* header */
  .site-header { left: 0; top: 0; width: 736px; height: 60px; background: var(--sand); border-bottom: 1px solid var(--sand-line); }
  .brand { left: 128px; top: 10px; color: var(--orange); font-family: "Short Stack", cursive; line-height: 1; }
  .brand-mark { display: inline-block; width: 12px; height: 12px; border-radius: 50%; background: var(--orange); vertical-align: middle; margin-right: 4px; }
  .brand-name { font-size: 15px; vertical-align: middle; }
  .brand-sub { display: block; font-size: 9px; margin: 3px 0 0 16px; letter-spacing: 1px; }
  .main-nav { left: 282px; top: 26px; display: flex; gap: 11px; font-family: "Arvo", serif; font-size: 10px; }
  .main-nav a { color: var(--orange); text-decoration: none; padding: 3px 0; }
  .main-nav a.active { background: var(--forest); color: var(--white); padding: 3px 8px; }

  /* hero */
  .hero { left: 0; top: 61px; width: 736px; height: 151px; background: var(--sand); }
  .photo { background: linear-gradient(160deg, #e9b07a, #c9834b); }
  .hero-kids-left { left: 122px; top: 5px; width: 95px; height: 120px; border-radius: 40px 40px 8px 8px; background: linear-gradient(180deg, #e9a14a, #d9d3c6); }
  .hero-title { left: 226px; top: 50px; font-family: "Schoolbell", cursive; font-size: 20px; letter-spacing: 1px; }
  .hero-title .fun { color: var(--pink); }
  .hero-title .act { color: var(--sky-blue); }
  .hero-kids-right { left: 390px; top: 6px; width: 238px; height: 140px; border-radius: 60px 60px 6px 6px; background: linear-gradient(100deg, #4cc0cf 0%, #e9553c 45%, #f3d6c7 80%, #c7b9a9 100%); }

  /* about */
  .about { left: 0; top: 212px; width: 736px; height: 190px; background: var(--mint); }
  .about-title { left: 118px; top: 30px; font-size: 13px; color: var(--forest); }
  .about-lead { left: 118px; top: 54px; font-size: 8.5px; line-height: 10px; color: var(--orange); }
  .about-text { left: 118px; top: 98px; width: 371px; font-size: 7.8px; line-height: 10.5px; text-align: justify; color: var(--ink); }
  .btn { display: inline-block; background: var(--forest); color: var(--white); font-family: "Schoolbell", cursive; text-transform: uppercase; font-size: 8px; padding: 2px 7px; border: 1px solid var(--white); }
  .about-more { left: 118px; top: 163px; }
  .about-illustration { left: 508px; top: 46px; width: 111px; height: 97px; border-radius: 45px; background: radial-gradient(circle at 40% 40%, #f6d36b, #e8743a 70%, #b3e6cb 72%); }

  /* activities */
  .activities { left: 0; top: 402px; width: 736px; height: 192px; background: var(--white); }
  .splat-left { left: 0; top: 0; width: 80px; height: 95px; border-radius: 0 50px 50px 0; background: #ee7b86; opacity: .85; }
  .splat-right { left: 665px; top: 130px; width: 71px; height: 62px; border-radius: 40px 0 0 0; background: #7ddc6f; }
  .activities-title { left: 118px; top: 20px; font-size: 13px; color: var(--forest); }
  .slider-arrows { left: 596px; top: 23px; display: flex; gap: 1px; }
  .slider-arrows span { display: block; width: 12px; height: 11px; background: var(--forest); }
  .slider-arrows svg { display: block; }
  .activity { top: 58px; width: 114px; }
  .activity .thumb { width: 114px; height: 96px; border: 1px solid #c9c9c9; }
  .activity .caption { margin-top: 5px; text-align: center; font-size: 10px; color: var(--orange); }

  /* schedule */
  .schedule { left: 0; top: 594px; width: 736px; height: 131px; background: linear-gradient(100deg, #3c9a4e 0%, #4aa85a 50%, #3a9349 100%); }
  .schedule-title { left: 118px; top: 14px; font-size: 12.5px; color: var(--white); }
  .schedule-text { left: 118px; top: 37px; width: 500px; font-size: 8px; line-height: 10px; color: var(--white); }
  .contact-title { left: 118px; top: 64px; font-size: 12px; color: var(--white); text-transform: uppercase; }
  .field { top: 88px; height: 18px; background: var(--forest-dark); color: #cfe8d2; font-size: 8px; padding: 4px 5px; border: 1px solid #2a8a3d; }
  .submit { left: 461px; top: 88px; height: 18px; width: 38px; background: var(--orange); color: var(--white); font-family: "Schoolbell", cursive; text-transform: uppercase; font-size: 8.5px; text-align: center; padding-top: 3px; border: 1px solid var(--white); }

  /* info columns */
  .info { left: 0; top: 725px; width: 736px; height: 235px; background: var(--sand); }
  .col-title { top: 22px; font-size: 10.5px; }
  .news-title { left: 118px; color: var(--sky-blue); }
  .tips-title { left: 290px; color: var(--rose); }
  .testi-title { left: 464px; color: var(--sea); }
  .news-item { left: 118px; width: 160px; }
  .news-item .thumb { position: absolute; left: 0; top: 0; width: 45px; height: 45px; border: 1px solid #ccc; }
  .news-body { position: absolute; left: 54px; top: 0; width: 106px; }
  .news-head { font-family: "Schoolbell", cursive; text-transform: uppercase; font-size: 8px; line-height: 10px; color: var(--ink); }
  .news-date { font-size: 6px; margin: 2px 0 3px 2px; color: var(--muted); }
  .news-text { font-size: 7.5px; line-height: 9.5px; color: var(--muted); }
  .tips { left: 290px; top: 46px; width: 160px; list-style: none; }
  .tips li { position: relative; padding-left: 12px; font-size: 7.5px; line-height: 9.5px; color: var(--muted); margin-bottom: 6px; }
  .tips li::before { content: "★"; position: absolute; left: 0; top: 0; color: var(--orange); font-size: 7px; }
  .quote-open { left: 464px; top: 50px; font-family: Georgia, serif; font-size: 22px; color: #c9beaa; line-height: 1; }
  .quote-close { left: 596px; top: 118px; font-family: Georgia, serif; font-size: 22px; color: #c9beaa; line-height: 1; }
  .testimonial { left: 473px; top: 67px; width: 150px; font-size: 7.5px; line-height: 9.5px; color: var(--muted); }
  .testi-author { left: 480px; top: 127px; font-size: 7.5px; color: var(--orange); }
  .testi-author::before { content: ""; display: inline-block; width: 20px; border-top: 1px solid var(--orange); vertical-align: middle; margin-right: 5px; }

  /* footer */
  .footer { left: 0; top: 960px; width: 736px; height: 202px; background: linear-gradient(180deg, var(--sky-top), var(--sky-bottom) 60%, var(--sky-top)); }
  .grass { left: 0; top: 138px; width: 736px; height: 64px; background: linear-gradient(180deg, #7fd23a 0%, #3f9a22 55%, var(--field) 100%); }
  .foot-title { top: 25px; font-size: 10.5px; color: var(--orange); line-height: 11px; }
  .email-label { left: 118px; top: 45px; font-size: 8.5px; color: var(--muted); }
  .email-label b { color: var(--orange); font-weight: 400; }
  .email-input { left: 118px; top: 59px; width: 107px; height: 15px; background: #b9cdd4; border: 1px solid #a8bcc3; }
  .subscribe { left: 118px; top: 83px; }
  .family-photo { left: 245px; top: 57px; width: 116px; height: 76px; border: 1px solid #d6d6d6; background: linear-gradient(120deg, #f1e2cf, #d49b72 50%, #8fa4c4); }
  .photostream { left: 377px; top: 46px; display: grid; grid-template-columns: repeat(4, 22px); gap: 5px; }
  .photostream span { display: block; width: 22px; height: 22px; border: 1px solid var(--white); }
  .contact-list { left: 509px; top: 44px; list-style: none; }
  .contact-list li { display: flex; align-items: center; gap: 7px; font-size: 7.5px; color: var(--ink); margin-bottom: 11px; }
  .contact-list svg { width: 9px; height: 9px; fill: #555; }

  /* bottom bar */
  .bottom-bar { left: 0; top: 1162px; width: 736px; height: 38px; background: var(--sand); }
  .copyright { left: 118px; top: 11px; font-size: 8px; color: var(--ink); }
  .social { left: 512px; top: 9px; display: flex; gap: 4px; }
  .social span { display: block; width: 18px; height: 16px; border-radius: 2px; }
</style>
</head>
<body>
<div class="page">

  <header class="site-header abs">
    <div class="brand abs"><span class="brand-mark"></span><span class="brand-name">Pelora Vantu</span><span class="brand-sub">Child Care</span></div>
    <nav class="main-nav abs">
      <a class="active" href="#">Home</a>
      <a href="#">About</a>
      <a href="#">Programs</a>
      <a href="#">Parents</a>
      <a href="#">Gallery</a>
      <a href="#">Enrollment</a>
      <a href="#">Contact</a>
    </nav>
  </header>

  <section class="hero abs">
    <div class="hero-kids-left abs" role="img" aria-label="Two toddlers in playful costumes"></div>
    <div class="hero-title abs"><span class="fun">FUN</span> <span class="act">ACTIVITIES</span></div>
    <div class="hero-kids-right abs" role="img" aria-label="Young children playing with toys and building blocks"></div>
  </section>

  <section class="about abs">
    <h2 class="about-title heading abs">About Pelora Vantu Child Care</h2>
    <p class="about-lead abs">We provide care, learning and education services<br>for children under 24 months, toddlers and also preschool children</p>
    <p class="about-text abs">Nemo enim ipsam voluptatem quia voluptas sit aspernatur aut odit aut fugit, sed quia consequuntur magni dolores eos qui ratione voluptatem sequi nesciunt. Neque porro quisquam est, qui dolorem ipsum quia dolor sit amet, consectetur, adipisci velit, sed quia non numquam eius modi tempora incidunt ut labore et dolore magnam aliquam quaerat voluptatem.</p>
    <a class="btn about-more abs">Read more</a>
    <div class="about-illustration abs" role="img" aria-label="Illustration of two cartoon children playing with toys"></div>
  </section>

  <section class="activities abs">
    <div class="splat-left abs" role="img" aria-label="Pink paint splash"></div>
    <div class="splat-right abs" role="img" aria-label="Green paint splash"></div>
    <h2 class="activities-title heading abs">Our Activities</h2>
    <div class="slider-arrows abs">
      <span><svg width="12" height="11" viewBox="0 0 12 11"><path d="M7.5 2.5 4.5 5.5 7.5 8.5" fill="none" stroke="#fff" stroke-width="1.5"/></svg></span>
      <span><svg width="12" height="11" viewBox="0 0 12 11"><path d="M4.5 2.5 7.5 5.5 4.5 8.5" fill="none" stroke="#fff" stroke-width="1.5"/></svg></span>
    </div>
    <div class="activity abs" style="left:115px">
      <div class="thumb" role="img" aria-label="Children playing in a colourful preschool classroom" style="background:linear-gradient(135deg,#f0c45a,#3c7fd0 60%,#e5504f)"></div>
      <div class="caption">Preschool Curriculum</div>
    </div>
    <div class="activity abs" style="left:247px">
      <div class="thumb" role="img" aria-label="Toddlers playing outdoors with a toy" style="background:linear-gradient(135deg,#a9473a,#d9b27a 55%,#4a7fb5)"></div>
      <div class="caption">Toddler Care</div>
    </div>
    <div class="activity abs" style="left:377px">
      <div class="thumb" role="img" aria-label="Teacher drawing with children at a table" style="background:linear-gradient(135deg,#9b86b8,#e6b28e 50%,#4aa0c8)"></div>
      <div class="caption">Hand Drawings</div>
    </div>
    <div class="activity abs" style="left:507px">
      <div class="thumb" role="img" aria-label="Baby playing with a shape sorter toy" style="background:linear-gradient(135deg,#e9e2d6,#e59ac8 50%,#e5c23f)"></div>
      <div class="caption">Shape Shake</div>
    </div>
  </section>

  <section class="schedule abs" role="img" aria-label="Children playing in a classroom behind a green tint">
    <h2 class="schedule-title heading abs">Schedule a Visit</h2>
    <p class="schedule-text abs">Meet our passionate teachers, experience our curriculum, learn about our health and safety policies, and see children excited about learning.</p>
    <h3 class="contact-title heading abs">We 'll contact you :</h3>
    <div class="field abs" style="left:118px;width:76px">First Name</div>
    <div class="field abs" style="left:199px;width:76px">Last Name</div>
    <div class="field abs" style="left:281px;width:75px">Email</div>
    <div class="field abs" style="left:368px;width:76px">Zip Code</div>
    <div class="submit abs">Submit</div>
  </section>

  <section class="info abs">
    <h3 class="col-title news-title heading abs">Latest News</h3>
    <h3 class="col-title tips-title heading abs">Parenting Tips</h3>
    <h3 class="col-title testi-title heading abs">Testimonials</h3>

    <article class="news-item abs" style="top:47px">
      <div class="thumb" role="img" aria-label="Children in a classroom" style="background:linear-gradient(135deg,#c8a66f,#5c8fc0)"></div>
      <div class="news-body">
        <div class="news-head">Quis aute irure dolor in reprehenderit</div>
        <div class="news-date">5 November,2015</div>
        <div class="news-text">Excepteur sint occaecat cupidatat non proident, sunt in culpa.</div>
      </div>
    </article>
    <article class="news-item abs" style="top:128px">
      <div class="thumb" role="img" aria-label="Child painting with bright colours" style="background:linear-gradient(135deg,#f2c54b,#e46b5b 50%,#6bb4e0)"></div>
      <div class="news-body">
        <div class="news-head">Vel illum qui dolorem eum fugiat</div>
        <div class="news-date">3rd November,2015</div>
        <div class="news-text">Quis autem vel eum iure reprehenderit qui in ea voluptate.</div>
      </div>
    </article>

    <ul class="tips abs">
      <li>Modi tempora incidunt ut labore magnam aliquam quaerat .</li>
      <li>Nemo enim ipsam voluptatem quia sit aspernatur aut odit aut fugit.</li>
      <li>Temporibus autem quibusdam et aut officiis debitis.</li>
      <li>Consectetur adipiscing elit sed do tempor incididunt ut labore et magna aliqua.</li>
      <li>Duis aute irure dolor &nbsp;in voluptate velit esse cillum.</li>
    </ul>

    <div class="quote-open abs">“</div>
    <p class="testimonial abs">Neque porro quisquam est, qui ipsum quia dolor sit amet consectetur. Adipisci velit, sed quia non numquam eius modi tempora incidunt ut labore et dolore magnam aliquam.</p>
    <div class="quote-close abs">”</div>
    <div class="testi-author abs">Mira Talen</div>
  </section>

  <footer class="footer abs" role="img" aria-label="Blue sky with soft clouds above a grass field">
    <div class="grass abs"></div>

    <h3 class="foot-title heading abs" style="left:118px">Newsletter</h3>
    <div class="email-label abs">Email <b>*</b></div>
    <div class="email-input abs"></div>
    <a class="btn subscribe abs">Subscribe!</a>

    <h3 class="foot-title heading abs" style="left:245px;width:120px">Family Resources for Growing Children</h3>
    <div class="family-photo abs" role="img" aria-label="Parents doing crafts with their child at a table"></div>

    <h3 class="foot-title heading abs" style="left:377px">Photostreams</h3>
    <div class="photostream abs" role="img" aria-label="Grid of twelve photos of children">
      <span style="background:#d98a5a"></span><span style="background:#c96a5a"></span><span style="background:#e0a37a"></span><span style="background:#8a9a6a"></span>
      <span style="background:#9aa35a"></span><span style="background:#b5835f"></span><span style="background:#7a8fa8"></span><span style="background:#e2b07f"></span>
      <span style="background:#c9a36f"></span><span style="background:#8fbf7a"></span><span style="background:#d69a82"></span><span style="background:#c7b3a3"></span>
    </div>

    <h3 class="foot-title heading abs" style="left:509px">Contact</h3>
    <ul class="contact-list abs">
      <li><svg viewBox="0 0 10 10"><path d="M5 0a3.5 3.5 0 0 0-3.5 3.5C1.5 6 5 10 5 10s3.5-4 3.5-6.5A3.5 3.5 0 0 0 5 0zm0 5a1.4 1.4 0 1 1 0-2.8A1.4 1.4 0 0 1 5 5z"/></svg>Lorem ipsum dolor sit amet</li>
      <li><svg viewBox="0 0 10 10"><path d="M2 0 4 2.5 3 4c.6 1.3 1.7 2.4 3 3l1.5-1L10 8 8.5 10C4 10 0 6 0 1.5z"/></svg>321 555 0147</li>
      <li><svg viewBox="0 0 10 10"><path d="M0 2h10v6H0zM0 2l5 3.5L10 2" stroke="#eee" stroke-width=".6"/></svg>mail@peloravantu.example</li>
    </ul>
  </footer>

  <div class="bottom-bar abs">
    <div class="copyright abs">© copyright information here</div>
    <div class="social abs">
      <span style="background:#3b5b9a"></span>
      <span style="background:#2aa6d8"></span>
      <span style="background:#1e78b4"></span>
      <span style="background:#d8332e"></span>
      <span style="background:#e8711a"></span>
    </div>
  </div>

</div>
</body>
</html>
```